Business Card Design for Massage Therapist

*I am a qualified massage therapist & require a business card for my new business 'Tidal Touch & Wellness'.
*Contact details I'd like included on the card are: Elise Brantry, Mobile: 0481562930, Email: tidaltw@mailvane.com
*It is a massage business dedicated to providing quality therapeutic massage treatments, that will later incorporate natural therapies.
* Styles Include: Swedish, Relaxation, Pregnancy, Deep Tissue & Sports Massage
*I offer the styles of massage as listed above & a mobile service that allows clients to book a massage in the comfort of their own home.
*I'd like my logo to be fairly simple, streamlined, modern & reflect what my business services are - one people will easily remember.
*I'd like the colors to represent & emit a sense of calm, be fresh, welcoming, natural colors that appeal to a wide range of people.
*Colors I'd like to see are: pale blue, aqua & greens.

Target Market(s)

Both Male & Female, aged 20 to 65, singles, couples, parents, business people who are interested in their health, fitness & general wellbeing and maintenance. Located in the Harbourvale area and surrounding suburbs of Melbourne.

Industry/Entity Type

Massage

Requirements
Must have
• Fonts used in logos should be owned by the designer.
Should not have
• I don't want the design to have someone being massaged in it (pictures/photos) or have it look too clinical & sterile.

```html
<!DOCTYPE html>
<html lang="en">
<head>
<meta charset="utf-8">
<title>Tidal Touch &amp; Wellness — Business Card</title>
<link rel="stylesheet" href="https://fonts.googleapis.com/css2?family=Marcellus&family=Open+Sans:wght@400;600;700&display=swap">
<style>
  :root {
    --backdrop: #c6c6c6;
    --card-front: #f3f3f3;
    --card-back: #ffffff;
    --aqua-green: #00a98a;
    --soft-green: #8fcfa8;
    --pale-blue: #9fd6f5;
    --ink: #3d3d3d;
    --white: #ffffff;
  }
  * { box-sizing: border-box; margin: 0; padding: 0; }
  html, body { width: 1200px; height: 900px; overflow: hidden; }
  body {
    background: var(--backdrop);
    font-family: "Open Sans", Arial, sans-serif;
    position: relative;
  }
  .card {
    position: absolute;
    width: 520px;
    height: 300px;
    overflow: hidden;
    box-shadow: 0 6px 18px rgba(0,0,0,0.18);
  }

  /* Front */
  .card-front { left: 60px; top: 470px; background: var(--card-front); }
  .card-front .brand { position: absolute; left: 0; right: 0; top: 92px; justify-content: center; }
  .card-front .footer-band {
    position: absolute; left: 0; right: 0; bottom: 0; height: 66px;
    background: var(--aqua-green);
  }

  .brand { display: flex; align-items: center; gap: 12px; }
  .brand-square { width: 26px; height: 26px; background: var(--aqua-green); flex: none; }
  .brand-name {
    font-family: "Marcellus", Georgia, serif;
    font-size: 26px;
    color: var(--ink);
    font-weight: 400;
    white-space: nowrap;
  }

  /* Back */
  .card-back { left: 620px; top: 140px; background: var(--card-back); }
  .therapist { position: absolute; left: 150px; top: 22px; color: var(--aqua-green); }
  .therapist-name { font-size: 13px; font-weight: 700; line-height: 1.2; }
  .therapist-role { font-size: 11px; font-weight: 400; }

  .services {
    position: absolute; left: 118px; top: 82px;
    list-style: none; color: var(--aqua-green);
    font-size: 11.5px; font-weight: 600; line-height: 16px;
  }
  .services li { display: flex; align-items: center; gap: 5px; }
  .services li::before {
    content: ""; width: 6px; height: 6px; border-radius: 50%;
    border: 1.5px solid var(--soft-green);
  }

  .card-back .brand { position: absolute; right: 22px; top: 118px; }
  .card-back .brand-name { font-size: 23px; }
  .card-back .brand-square { width: 22px; height: 22px; }

  .contact-bar {
    position: absolute; left: 0; top: 170px; width: 222px; height: 72px;
    background: var(--aqua-green);
    border-radius: 0 12px 12px 0;
    padding: 14px 0 0 18px;
    color: var(--white); font-size: 12px; line-height: 20px;
  }
  .contact-line { display: flex; align-items: center; gap: 8px; }
  .contact-line svg { width: 11px; height: 11px; flex: none; }

  .accent-pill { position: absolute; top: 176px; height: 60px; border-radius: 10px; }
  .pill-green { left: 234px; width: 44px; background: var(--aqua-green); }
  .pill-soft { left: 288px; width: 34px; background: var(--soft-green); }
  .pill-blue { left: 332px; width: 20px; background: var(--pale-blue); }
</style>
</head>
<body>

  <section class="card card-front" aria-label="Card front">
    <div class="brand">
      <span class="brand-square"></span>
      <span class="brand-name">Tidal Touch &amp; Wellness</span>
    </div>
    <div class="footer-band"></div>
  </section>

  <section class="card card-back" aria-label="Card back">
    <div class="therapist">
      <p class="therapist-name">Elise Brantry</p>
      <p class="therapist-role">Massage Therapist</p>
    </div>

    <ul class="services">
      <li>Swedish,</li>
      <li>Relaxation,</li>
      <li>Pregnancy,</li>
      <li>Deep Tissue</li>
      <li>Sports Massage</li>
    </ul>

    <div class="brand">
      <span class="brand-square"></span>
      <span class="brand-name">Tidal Touch &amp; Wellness</span>
    </div>

    <div class="contact-bar">
      <p class="contact-line">
        <svg viewBox="0 0 24 24" aria-hidden="true"><path fill="#fff" d="M6.6 10.8a15 15 0 0 0 6.6 6.6l2.2-2.2c.3-.3.7-.4 1-.2 1.1.4 2.3.6 3.6.6.6 0 1 .4 1 1V20c0 .6-.4 1-1 1A17 17 0 0 1 3 4c0-.6.4-1 1-1h3.5c.6 0 1 .4 1 1 0 1.3.2 2.5.6 3.6.1.3 0 .7-.2 1z"/></svg>
        0481562930,
      </p>
      <p class="contact-line">
        <svg viewBox="0 0 24 24" aria-hidden="true"><rect x="2" y="5" width="20" height="14" rx="2" fill="none" stroke="#fff" stroke-width="2"/><path d="M3 6l9 7 9-7" fill="none" stroke="#fff" stroke-width="2"/></svg>
        tidaltw@mailvane.com
      </p>
    </div>

    <span class="accent-pill pill-green"></span>
    <span class="accent-pill pill-soft"></span>
    <span class="accent-pill pill-blue"></span>
  </section>

</body>
</html>
```